◆遺体の目的/概要
電子書籍(novrel)の表紙のデザインをお願いします。

◆画像のサイズ
表紙ファイルの理想的な寸法は2,560✕1,600ピクセルです。
注:画像の寸法は1,000✕625ピクセル以上であることが必要です。
画像の最大の寸法は10,000✕10,000ピクセルです。

◆タイトル
外国人と一緒に働くすべての人へ
「ソラーレ・ポルト・メトリクス」
Solare Porto Metrics
少子高齢化の社会を生き残る強い会社を作る方法

◆著者
外国人ブリッジコーディネーター
橋本 健吾

◆本の内容
少子高齢化が進む社会にあって、
外国人労働者の必要性や、彼らが働きやす職場環境作りの必要性
どんなコミュニケーションが必要かという事を解説した本です。
※本文を参考資料として添付します。

◆デザイン要望
会社や企業向けなので、プロフェッショナルなイメージ
グローバルなイメージ(目を引く外国人の写真など)
でよろしくお願い致します。

※次点、次々点の方への参加報酬も設定いたします。

※その他、必要な情報がありましたらお問い合せください。

本文の内容に該当する登場人物のイメージを用いている点や
「強い会社を作る」という主なテーマが強調されていいる点など、
ぱっと見て分かりやすいものを選ばせていただきました。

ほんとにどれもセンスを感じられるものだったので、
選定するのに、とても時間がかかりました。
同じテーマで、こんなにも色々なアイデアがあること
その多様性に感動しました。
皆さんが時間をかけて、考えてくださったことに感謝致します。
今後も出版を考えていますので、また依頼の際は多くの方の提案をよろしくお願い致します!

```html
<!DOCTYPE html>
<html lang="ja">
<head>
<meta charset="UTF-8">
<title>ソラーレ・ポルト・メトリクス</title>
<link rel="stylesheet" href="https://fonts.googleapis.com/css2?family=Noto+Sans+JP:wght@700;900&family=Noto+Serif+JP:wght@600;700;900&family=Open+Sans:wght@500;600&display=swap">
<style>
  :root {
    --navy-deep: #0a1a4a;
    --navy: #13307a;
    --blue: #1f56b8;
    --blue-bright: #2f6fd6;
    --steel: #6f7f9c;
    --white: #ffffff;
    --faint: rgba(255,255,255,0.22);
    --rule: rgba(255,255,255,0.85);
  }
  * { margin: 0; padding: 0; box-sizing: border-box; }
  html, body { width: 750px; height: 1200px; overflow: hidden; background: var(--navy-deep); }
  .cover {
    position: relative;
    width: 750px;
    height: 1200px;
    overflow: hidden;
    background: linear-gradient(180deg, #5f7190 0%, #3a5590 12%, var(--blue) 30%, var(--blue-bright) 45%, var(--navy) 68%, var(--navy-deep) 100%);
    color: var(--white);
    text-align: center;
  }
  .hero-visual {
    position: absolute;
    left: 90px; top: 90px;
    width: 570px; height: 660px;
    background: radial-gradient(ellipse at 50% 45%, rgba(170,190,220,0.45) 0%, rgba(80,120,190,0.25) 45%, rgba(31,86,184,0) 75%);
  }
  .corner-piece {
    position: absolute;
    bottom: 0;
    width: 110px; height: 120px;
    background: linear-gradient(160deg, #c9ced8, #8a93a6);
    opacity: 0.8;
  }
  .corner-piece.left { left: 0; }
  .corner-piece.right { right: 0; }
  .backdrop-word {
    position: absolute;
    top: -28px; left: 0; right: 0;
    font-family: "Noto Serif JP", serif;
    font-weight: 600;
    font-size: 168px;
    letter-spacing: 14px;
    color: var(--faint);
    line-height: 1;
  }
  .tagline {
    position: absolute;
    top: 232px; left: 0; right: 0;
    font-family: "Noto Serif JP", serif;
    font-weight: 700;
    font-size: 35px;
    letter-spacing: 2px;
  }
  .title {
    position: absolute;
    left: 0; right: 0;
    font-family: "Noto Sans JP", sans-serif;
    font-weight: 900;
    font-size: 70px;
    letter-spacing: 2px;
    line-height: 1;
  }
  .title.line-1 { top: 385px; }
  .title.line-2 { top: 563px; }
  .title-en {
    position: absolute;
    top: 465px; left: 80px; right: 80px;
    padding: 12px 0;
    border-top: 2px solid var(--rule);
    border-bottom: 2px solid var(--rule);
    font-family: "Open Sans", sans-serif;
    font-weight: 600;
    font-size: 33px;
    line-height: 1.2;
  }
  .subtitle {
    position: absolute;
    top: 855px; left: 0; right: 0;
    font-family: "Noto Serif JP", serif;
    font-weight: 900;
    font-size: 45px;
    line-height: 1.58;
    letter-spacing: 3px;
  }
  .author-role {
    position: absolute;
    top: 1038px; left: 0; right: 0;
    font-family: "Noto Serif JP", serif;
    font-weight: 700;
    font-size: 27px;
  }
  .author-name {
    position: absolute;
    top: 1085px; left: 0; right: 0;
    font-family: "Noto Serif JP", serif;
    font-weight: 700;
    font-size: 34px;
    letter-spacing: 2px;
  }
</style>
</head>
<body>
  <main class="cover">
    <div class="hero-visual" role="img" aria-label="パズルのピースが組み合わさる中に浮かぶ外国人ビジネスパーソンの写真"></div>
    <div class="corner-piece left" role="img" aria-label="パズルピースの装飾"></div>
    <div class="corner-piece right" role="img" aria-label="パズルピースの装飾"></div>
    <div class="backdrop-word" aria-hidden="true">GLOBAL</div>

    <p class="tagline">外国人と一緒に働くすべての人へ</p>
    <h1 class="title line-1">ソラーレ・ポルト・</h1>
    <p class="title-en">Solare Porto Metrics</p>
    <p class="title line-2">メトリクス</p>

    <p class="subtitle">少子高齢化の社会を生き残る<br>強い会社を作る方法</p>

    <p class="author-role">外国人ブリッジコーディネーター</p>
    <p class="author-name">橋本 健吾</p>
  </main>
</body>
</html>
```